Halloway's Events

This is a brochure to promotoe our party, event planning, meeting, rooms and capabilities.

THE ANVIL HALL
Halloway’s Party, Function, Meeting, & Event Venue
When you plan a business meeting, conference, social gathering or event at Halloway’s tavern and Grill, you can feel confident it will be successful as well as unforgettable.
First, our Restaurant itself offers a impressive, tastefully designed meeting space, plus a number of amenities that are attractive to both meeting planners and attendees. Second, our restaurant’s on-site Management and Chef staff is comprised of dedicated professionals who’ll make sure your event goes off without a hitch.
A Fabulous Florida Celtic Tavern and Grill
The location of a meeting can make or break it. That’s partly why Halloway’s has been so popular with individuals, meeting professionals and attendees. We are easily accessed by car, with ample onsite parking, and Free Garage parking. We are located within the Meridian Square Plaza, boasting over 5,000 sq ft of Restaurant space for your next Party or event, including private function rooms, (The Kiln), with full AV capability, private bar, and seating for over 50 and standing capacity up to 80.
Corporate Meeting Facilities
At Halloway’s, we can accommodate groups ranging from 10 to 200 attendees. We offer 5,000 square feet of newly renovated, elegantly appointed Restaurant space with private Break out room available. Options include dinner or lunch service, boardroom, meeting space, full AV capabilities, appetizers, set menu’s, live music and additional entertainment options.We also offer outdoor space that offer the best South Florida has to offer.

Supportive Staff and Event Packages
At Halloway’s, our experienced on-property Management and Culinary staff will help every step of the way, including planning the most efficient use of meeting space, meals, receptions, entertainment, registration and audiovisual needs. When it’s time for a break from work, our staff can also help with group recreation opportunities and teambuilding exercises, such as a fun themed parties, karaoke, Trivia, or the event of your choosing.
A great place to start your meeting or event planning is by checking out the THE ANVIL HALL meeting space on our web site, www.hwbpub.example, our stop in and speak with one of management or culinary staff members, or simply call us on 1-561-555-0148.
We promise your event will be unforgettable!
We look forward to being in service to you - Cead Mile Failte (one hundred thousand welcomes)
Slainte!

Spec's TRI fold Brochure full color two sides from pressly co

Full Bleed Size (starting document size)

11.10" x 8.63"
282 x 219 mm
3331 x 2588 pixels

* Finished artwork should use the full bleed dimensions for best results.

Document Trim Size (final size after being cut)

10.98" x 8.50"
279 x 216 mm
3295 x 2551 pixels

* Please be sure to keep all text within the safe margin.

Resolution

300 DPI

* Dotted lines indicate where a fold will take place. If you don’t want copy or design to appear on the fold, make sure they stay within each panel’s safe margin.

Target Market(s)

Individuals, Comapanies, Meet up groups, and event planners.

Industry/Entity Type

Event Planning

Requirements
Must have
• Logo, description of our events, address and web site

2740 Pelican Ave., Suite 210
Boynton Beach, Florida 33400
PH:1-561-555-0148
email: hwbpub@mailbox.example
web www.hwbpub.example
FREE GARAGE PARKING
(Just east of Halvern in the Meridian Square Plaza near Brewlark and the Grape Vault)
Hours of Operation
Sun-Thurs 11:30am - Midnight
Fri - Sat 11:30am - 2:00am
Nice to have
• FUN PHOTOS AND INCORPORATE FOOD WHERE POSSIBLE FESTIVE

```html
<!DOCTYPE html>
<html lang="en">
<head>
<meta charset="utf-8">
<title>The Anvil Hall – Halloway's Events Brochure</title>
<link rel="stylesheet" href="https://fonts.googleapis.com/css2?family=EB+Garamond:wght@400;500;600;700&display=swap">
<style>
  :root {
    --ink: #000000;
    --paper: #ffffff;
    --cream: #f4efe4;
    --brown-deep: #2a1c10;
    --brown-mid: #4a3420;
    --gold-light: #e8d08a;
    --gold: #b8923e;
    --gold-dark: #6e5320;
    --copper-light: #c89a84;
    --copper-dark: #6a4536;
  }
  * { box-sizing: border-box; margin: 0; padding: 0; }
  html, body {
    width: 1200px; height: 927px; overflow: hidden;
    background: var(--ink);
  }
  .brochure {
    position: relative; width: 1200px; height: 927px;
    background: var(--ink);
    font-family: "EB Garamond", Garamond, Georgia, serif;
    color: var(--paper);
  }
  .hero-photo {
    position: absolute; left: 0; top: 0; width: 425px; height: 660px;
    background:
      radial-gradient(ellipse at 30% 35%, rgba(240,200,120,.85) 0%, rgba(180,120,50,.6) 30%, rgba(60,35,15,0) 65%),
      radial-gradient(ellipse at 75% 30%, rgba(230,190,110,.7) 0%, rgba(120,70,30,0) 50%),
      linear-gradient(180deg, #3a2412 0%, #5a3a1c 55%, #2a1a0c 100%);
  }
  .middle-wash {
    position: absolute; left: 425px; top: 0; width: 380px; height: 660px;
    background: linear-gradient(180deg, #2e2014 0%, #241a10 50%, #120c06 85%, var(--ink) 100%);
  }
  .venue-title {
    position: absolute; left: 22px; top: 44px;
    font-size: 37px; font-weight: 600; letter-spacing: .3px;
    color: var(--cream);
    text-shadow: 1px 2px 3px rgba(0,0,0,.7);
  }
  .venue-tagline {
    position: absolute; left: 35px; top: 470px; width: 330px;
    font-size: 33px; font-weight: 600; line-height: 38px;
    color: var(--paper);
    text-shadow: 1px 2px 3px rgba(0,0,0,.6);
  }
  .copy p {
    font-size: 14px; line-height: 19.2px; text-align: justify;
    margin-bottom: 19px;
  }
  .intro { position: absolute; left: 35px; top: 680px; width: 352px; }
  .intro p { font-size: 14px; line-height: 19px; text-align: left; }
  .column-middle { position: absolute; left: 442px; top: 48px; width: 326px; }
  .column-right { position: absolute; left: 838px; top: 322px; width: 326px; }
  .column-right p { font-weight: 500; font-size: 13.6px; line-height: 19px; }
  .section-heading {
    font-size: 16.5px; font-weight: 600; margin-bottom: 19px;
  }
  .column-right .section-heading { font-size: 21px; font-weight: 500; margin-bottom: 24px; }
  .frame {
    position: absolute;
    padding: 16px;
    background: linear-gradient(135deg, var(--gold-light) 0%, var(--gold) 30%, var(--gold-dark) 55%, var(--gold) 75%, var(--gold-light) 100%);
    box-shadow: 0 0 0 2px var(--gold-dark) inset;
  }
  .frame--copper {
    background: linear-gradient(135deg, var(--copper-light) 0%, #a2725e 35%, var(--copper-dark) 60%, #a2725e 80%, var(--copper-light) 100%);
  }
  .frame--wide { padding: 28px 26px; }
  .frame .photo { width: 100%; height: 100%; box-shadow: 0 0 0 3px rgba(0,0,0,.35); }
  .frame-dining { left: 833px; top: 45px; width: 330px; height: 263px; }
  .frame-food { left: 425px; top: 533px; width: 355px; height: 367px; padding: 24px 72px 26px 72px; }
  .frame-meeting { left: 835px; top: 652px; width: 328px; height: 250px; }
  .photo-dining { background: linear-gradient(180deg, #d8c8a4 0%, #9c6a44 50%, #6a3a26 100%); }
  .photo-food { background: radial-gradient(circle at 45% 45%, #e6b45a 0%, #c08a3a 35%, #f0ece4 60%, #2a2420 100%); }
  .photo-meeting { background: linear-gradient(160deg, #4a3a30 0%, #6e5a4c 45%, #d8d0c4 75%, #3a2e28 100%); }
</style>
</head>
<body>
<main class="brochure">
  <div class="hero-photo" role="img" aria-label="Two champagne flutes with golden streamers and sparkles"></div>
  <div class="middle-wash"></div>

  <h1 class="venue-title">THE ANVIL HALL</h1>
  <h2 class="venue-tagline">Halloway’s Party, Function, Meeting, &amp; Event Venue</h2>

  <section class="intro copy">
    <p>When you plan a business meeting, conference, social gathering or event at Halloway’s tavern and Grill, you can feel confident it will be successful as well as unforgettable.</p>
    <p>First, our Restaurant itself offers a impressive, tastefully designed meeting space, plus a number of amenities that are attractive to both meeting planners and attendees.</p>
    <p>Second, our restaurant’s on-site Management and Chef staff is comprised of dedicated professionals who’ll make sure your event goes off without a hitch.</p>
  </section>

  <section class="column-middle copy">
    <h3 class="section-heading">A Fabulous Florida Celtic Tavern and Grill</h3>
    <p>The location of a meeting can make or break it. That’s partly why Halloway’s has been so popular with individuals, meeting professionals and attendees. We are easily accessed by car, with ample onsite parking, and Free Garage parking. We are located within the Meridian Square Plaza, boasting over 5,000 sq ft of Restaurant space for your next Party or event, including private function rooms, (The Kiln), with full AV capability, private bar, and seating for over 50 and standing capacity up to 80.</p>
    <h3 class="section-heading">Corporate Meeting Facilities</h3>
    <p>At Halloway’s, we can accommodate groups ranging from 10 to 200 attendees. We offer 5,000 square feet of newly renovated, elegantly appointed Restaurant space with private Break out room available. Options include dinner or lunch service, boardroom, meeting space, full AV capabilities, appetizers, set menu’s, live music and additional entertainment options. We also offer outdoor space that offer the best South Florida has to offer.</p>
  </section>

  <div class="frame frame-food">
    <div class="photo photo-food" role="img" aria-label="Plates of fried fish, fries, loaded nachos and appetizers"></div>
  </div>

  <div class="frame frame-dining frame--wide">
    <div class="photo photo-dining" role="img" aria-label="Tavern dining room with wooden tables and a bar"></div>
  </div>

  <section class="column-right copy">
    <h3 class="section-heading">Supportive Staff and Event Packages</h3>
    <p>At Halloway’s, our experienced on-property Management and Culinary staff will help every step of the way, including planning the most efficient use of meeting space, meals, receptions, entertainment, registration and audiovisual needs. When it’s time for a break from work, our staff can also help with group recreation opportunities and teambuilding exercises, such as a fun themed parties, karaoke, Trivia, or the event of your choosing.</p>
    <p>A great place to start your meeting or event planning is by checking out the The Kiln room meeting space on our web site, www.hwbpub.example, our stop in and speak with one of management or culinary staff members, or simply call us on 1-561-555-0148.</p>
  </section>

  <div class="frame frame-meeting frame--copper">
    <div class="photo photo-meeting" role="img" aria-label="Business team gathered around a table reviewing plans"></div>
  </div>
</main>
</body>
</html>
```